Business Card Design Project

we are a new company , see www.chatbridgeflow.com
we also have a concurrent flyer deign competition so you may also wish to enter that.
We provide live customer support services for websites.
We cater for mainly european market.
info for card:
Martin Colbrook
Director
p: +353 (0)90 517 2861
f: +353 (0)90 517 2872
m: +353 (0)86 908 4523
e: martin@chatbridgeflow.com
w: www.chatbridgeflow.com
The card does not have to use the exact colour on the website but should ahve something of the general feel of it. It should have modern corporate feel without brash coulours. we will upload the logo and card should be standard european size 85x55mm
Target Market(s)
Online business owners
Industry/Entity Type
Business
Look and feel
Each slider illustrates characteristics of the customer's brand and the style your logo design should communicate.

```html
<!DOCTYPE html>
<html lang="en">
<head>
<meta charset="utf-8">
<title>ChatBridge Flow – Business Card</title>
<link rel="stylesheet" href="https://fonts.googleapis.com/css2?family=Jura:wght@400;500&family=Arimo:wght@400;700&display=swap">
<style>
  :root {
    --stage-top: #dcdcdc;
    --stage-bottom: #f5f5f5;
    --card-white: #ffffff;
    --panel-top: #3183b5;
    --panel-bottom: #124a74;
    --back-light: #c4eef7;
    --back-mid: #86cde2;
    --back-deep: #3f8db8;
    --ink-light: #ffffff;
    --ink-soft: #d8ebf6;
    --brand-ink: #3b4046;
  }
  * { box-sizing: border-box; margin: 0; padding: 0; }
  html, body { width: 907px; height: 1200px; overflow: hidden; }
  body {
    position: relative;
    background: linear-gradient(180deg, var(--stage-top) 0%, var(--stage-bottom) 45%, var(--stage-bottom) 100%);
    font-family: "Arimo", Arial, sans-serif;
  }
  .card {
    position: absolute;
    left: 88px;
    width: 733px;
    height: 476px;
    border-radius: 40px;
    overflow: hidden;
    box-shadow: 0 2px 6px rgba(0,0,0,0.12);
  }
  .card--front { top: 101px; background: var(--card-white); }
  .card--back {
    top: 620px;
    background:
      radial-gradient(circle at 22% 18%, rgba(255,255,255,0.35) 0, rgba(255,255,255,0.08) 22%, rgba(255,255,255,0) 38%),
      linear-gradient(60deg, var(--back-light) 0%, var(--back-mid) 45%, var(--back-deep) 100%);
  }
  .contact-panel {
    position: absolute;
    left: 0; top: 0;
    width: 403px; height: 100%;
    background: linear-gradient(180deg, var(--panel-top) 0%, var(--panel-bottom) 100%);
    color: var(--ink-light);
  }
  .person-name {
    position: absolute;
    left: 81px; top: 213px;
    font-family: "Jura", sans-serif;
    font-weight: 500;
    font-size: 33px;
    letter-spacing: 0.5px;
    line-height: 1;
  }
  .person-role {
    position: absolute;
    left: 81px; top: 254px;
    font-family: "Jura", sans-serif;
    font-weight: 500;
    font-size: 24px;
    line-height: 1;
  }
  .contact-list {
    position: absolute;
    left: 44px; top: 308px;
    list-style: none;
  }
  .contact-list li {
    display: flex;
    align-items: center;
    height: 29.5px;
    font-size: 22px;
    color: var(--ink-light);
  }
  .contact-icon {
    width: 24px; height: 22px;
    margin-right: 13px;
    fill: var(--ink-soft);
    flex: none;
  }
  .brand-name {
    position: absolute;
    font-family: "Arimo", Arial, sans-serif;
    font-weight: 700;
    color: var(--brand-ink);
    white-space: nowrap;
    transform: translate(-50%, -50%);
    letter-spacing: 0.5px;
  }
  .card--front .brand-name { left: 563px; top: 260px; font-size: 34px; }
  .card--back .brand-name { left: 367px; top: 236px; font-size: 52px; }
</style>
</head>
<body>
  <section class="card card--front">
    <div class="contact-panel">
      <p class="person-name">Martin Colbrook</p>
      <p class="person-role">Director</p>
      <ul class="contact-list">
        <li>
          <svg class="contact-icon" viewBox="0 0 24 22" aria-hidden="true"><path d="M2 6 Q12 0 22 6 L20 9 L16 8 L15 6 Q12 5 9 6 L8 8 L4 9 Z"/><rect x="5" y="11" width="14" height="9" rx="2"/></svg>
          +353 (0)90 517 2861
        </li>
        <li>
          <svg class="contact-icon" viewBox="0 0 24 22" aria-hidden="true"><rect x="6" y="1" width="12" height="8"/><rect x="2" y="9" width="20" height="11" rx="2"/></svg>
          +353 (0)90 517 2872
        </li>
        <li>
          <svg class="contact-icon" viewBox="0 0 24 22" aria-hidden="true"><rect x="8" y="1" width="9" height="20" rx="2"/><rect x="10" y="4" width="5" height="6" fill="#1d5a86"/></svg>
          +353 (0)86 908 4523
        </li>
        <li>
          <svg class="contact-icon" viewBox="0 0 24 22" aria-hidden="true"><text x="3" y="18" font-size="20" font-family="Arial, sans-serif">@</text></svg>
          martin@chatbridgeflow.com
        </li>
        <li>
          <svg class="contact-icon" viewBox="0 0 24 22" aria-hidden="true"><circle cx="12" cy="11" r="9"/><path d="M3 11 H21 M12 2 Q6 11 12 20 M12 2 Q18 11 12 20" stroke="#1d5a86" stroke-width="1.4" fill="none"/></svg>
          www.chatbridgeflow.com
        </li>
      </ul>
    </div>
    <p class="brand-name">ChatBridge Flow</p>
  </section>

  <section class="card card--back">
    <p class="brand-name">ChatBridge Flow</p>
  </section>
</body>
</html>
```